Sign Design

We already have a logo, but would like to design 2 x signs.
Sign 1:
Dimensions 1500mm wide x 2500m high.
Information to include on sign: - Clinic name and logo (attached)
- the word "DENTIST "
- Street number (which is 348)
Phone number (which is 6153 4097)

Sign 2:
Dimensions: 800mm wide x 600mm high

```html
<!DOCTYPE html>
<html lang="en">
<head>
<meta charset="utf-8">
<title>Larkfield Dental Care – Sign Designs</title>
<link href="https://fonts.googleapis.com/css2?family=Arimo:wght@400&family=Open+Sans:wght@400&display=swap" rel="stylesheet">
<style>
  :root {
    --leaf: #accd62;
    --forest: #33683a;
    --paper: #ffffff;
    --ink: #1a1a1a;
  }
  html, body {
    margin: 0;
    padding: 0;
    overflow: hidden;
    background: var(--paper);
  }
  .artboard {
    position: relative;
    width: 1200px;
    height: 911px;
    background: var(--paper);
    overflow: hidden;
  }
  .size-label {
    position: absolute;
    margin: 0;
    font-family: "Open Sans", sans-serif;
    font-size: 12px;
    color: var(--ink);
    line-height: 1;
  }
  .sign {
    position: absolute;
    display: block;
    box-sizing: border-box;
    border: 1px solid var(--ink);
  }
  .sign--tall { left: 200px; top: 187px; width: 325px; height: 542px; }
  .sign--wide { left: 588px; top: 332px; width: 387px; height: 290px; }
  .label--tall { left: 199px; top: 161px; }
  .label--wide { left: 590px; top: 303px; }
  .field { fill: var(--leaf); }
  .swoosh { fill: var(--paper); }
  .brand-dot { fill: var(--leaf); }
  .brand-name {
    fill: var(--forest);
    font-family: "Arimo", sans-serif;
    font-weight: 400;
    letter-spacing: -0.04em;
  }
  .headline {
    fill: var(--forest);
    font-family: "Arimo", sans-serif;
    font-size: 37px;
  }
  .contact {
    fill: var(--paper);
    font-family: "Arimo", sans-serif;
    font-size: 36px;
  }
  .icon { fill: var(--paper); }
  .divider { stroke: var(--paper); stroke-width: 1.5; }
</style>
</head>
<body>
<main class="artboard">
  <p class="size-label label--tall">1500mm x 2500m</p>
  <svg class="sign sign--tall" viewBox="0 0 325 542" xmlns="http://www.w3.org/2000/svg">
    <rect class="field" width="325" height="542"/>
    <path class="swoosh" d="M0 108 C80 55 180 30 232 37 Q290 40 325 49 L325 228 C240 285 140 305 84 300 Q30 298 0 288 Z"/>
    <circle class="brand-dot" cx="152" cy="128" r="46"/>
    <text class="brand-name" x="162" y="227" font-size="44" text-anchor="middle">Larkfield</text>
    <text class="brand-name" x="162" y="255" font-size="25" text-anchor="middle">Dental Care</text>
    <text class="headline" x="100" y="377">DENTIST</text>
    <path class="icon" d="M59 402 a10 10 0 0 1 10 10 c0 7 -10 16 -10 16 s-10 -9 -10 -16 a10 10 0 0 1 10 -10 z M59 408 a4 4 0 1 0 0.01 0 z"/>
    <line class="divider" x1="85" y1="398" x2="85" y2="484"/>
    <text class="contact" x="99" y="430">348</text>
    <path class="icon" d="M51 459 l5 -2 l4 8 l-3 3 c2 4 5 7 9 9 l3 -3 l8 4 l-2 5 c-1 2 -3 3 -5 2 c-10 -4 -18 -12 -21 -22 c-1 -2 0 -4 2 -4 z"/>
    <text class="contact" x="99" y="482">6153 4097</text>
  </svg>

  <p class="size-label label--wide">800mm x 600mm</p>
  <svg class="sign sign--wide" viewBox="0 0 387 290" xmlns="http://www.w3.org/2000/svg">
    <rect class="field" width="387" height="290"/>
    <path class="swoosh" d="M0 120 C90 50 200 20 281 23 Q340 26 387 41 L387 165 C300 230 180 262 102 259 Q40 256 0 240 Z"/>
    <circle class="brand-dot" cx="84" cy="150" r="46"/>
    <text class="brand-name" x="360" y="150" font-size="43" text-anchor="end">Larkfield</text>
    <text class="brand-name" x="344" y="175" font-size="25" text-anchor="end">Dental Care</text>
  </svg>
</main>
</body>
</html>
```